Professional Home Buyer business card needed

I need a pretty straight forward business card designed. We help people that NEED to sell their homes solve problems. We perform all types of Real Estate transactions including flip, wholesale, investment, rental property and multi family. The card will mainly be used to give to prospective Sellers but will also be given to Real Estate Investors as well. It should professional and very easy to read, most clients are older people.

Target Market(s)

Distressed home sellers as well as Real Estate investors

Industry/Entity Type

Real Estate

Contact Information for Business Card

should be a professional layout

Colors
ec1f27
ffffff
000000

Requirements
Must have
• Large logo on back and smaller one on front. should utilize Red, white, and black.
• I am thinking of using a soft touch coating on the card so keep that in mind.
• Contact info should be very easy to read, think older clients.
Nice to have
• I would like to see a design with rounded corners on the card
Should not have
• pictures of homes or other home graphics.

```html
<!DOCTYPE html>
<html lang="en">
<head>
<meta charset="utf-8">
<title>Summit Home Buyers – Business Card</title>
<link href="https://fonts.googleapis.com/css2?family=Archivo+Black&family=Crimson+Text:wght@400&family=Montserrat:wght@400;500&display=swap" rel="stylesheet">
<style>
  :root {
    --bg: #c0c0c0;
    --deep-red: #860000;
    --brand-red: #ec1f27;
    --white: #ffffff;
    --black: #000000;
    --ink: #1a1a1a;
    --silver-light: #e4e4e4;
    --silver-mid: #bdbdbd;
  }
  * { box-sizing: border-box; margin: 0; padding: 0; }
  html, body { width: 1200px; height: 1200px; overflow: hidden; }
  body { background: var(--bg); position: relative; font-family: "Montserrat", sans-serif; }

  .card {
    position: absolute;
    left: 179px;
    width: 840px;
    height: 480px;
    overflow: hidden;
    box-shadow: 0 6px 14px rgba(0,0,0,0.35);
  }

  /* Front */
  .card--front { top: 67px; background: var(--deep-red); color: var(--white); text-align: center; }
  .front__tagline {
    position: absolute; top: 128px; left: 0; right: 0;
    font-family: "Archivo Black", sans-serif; font-size: 17px; letter-spacing: 9px;
  }
  .front__name {
    position: absolute; top: 168px; left: 0; right: 0;
    font-family: "Archivo Black", sans-serif; font-size: 96px; line-height: 1; letter-spacing: 2px;
  }
  .front__sub {
    position: absolute; top: 316px; left: 0; right: 0;
    font-family: "Archivo Black", sans-serif; font-size: 38px; letter-spacing: 11px;
  }

  /* Back */
  .card--back { top: 631px; background: var(--silver-mid); }
  .back__hero {
    position: absolute; left: 0; top: 0; width: 840px; height: 256px;
    background: radial-gradient(ellipse at 60% 100%, #ff1010 0%, #c30000 45%, #8a0000 100%);
  }
  .back__slash { position: absolute; left: 0; top: 0; }
  .back__person { position: absolute; left: 398px; top: 70px; width: 310px; text-align: center; color: var(--white); font-family: "Crimson Text", serif; }
  .person__name { font-size: 58px; line-height: 1; letter-spacing: -1px; }
  .person__title { font-size: 36px; line-height: 1; margin-top: 4px; }
  .person__title::before, .person__title::after { content: "—"; }

  .back__info {
    position: absolute; left: 0; top: 256px; width: 840px; height: 164px;
    background: linear-gradient(170deg, var(--silver-light) 0%, #cfcfcf 50%, #b3b3b3 100%);
  }
  .contact { position: absolute; color: var(--ink); }
  .contact__phone { left: 93px; top: 11px; font-size: 29px; }
  .contact__email { left: 93px; top: 45px; font-size: 29px; }
  .contact__address { left: 94px; top: 81px; font-size: 18px; line-height: 23px; }
  .icon { position: absolute; }

  .mini-logo { position: absolute; left: 595px; top: 39px; width: 224px; text-align: center; color: var(--ink); font-family: "Archivo Black", sans-serif; }
  .mini-logo__tagline { font-size: 8px; letter-spacing: 3px; }
  .mini-logo__name { font-size: 34px; line-height: 1; margin-top: 8px; }
  .mini-logo__sub { font-size: 13px; letter-spacing: 4px; margin-top: 10px; }

  .back__web {
    position: absolute; left: 0; top: 420px; width: 840px; height: 37px;
    background: linear-gradient(100deg, #a8a8a8 0%, #f2f2f2 18%, #bdbdbd 40%, #ededed 62%, #b0b0b0 85%, #e6e6e6 100%);
    text-align: center; font-size: 27px; line-height: 37px; color: var(--ink);
  }
  .back__footer {
    position: absolute; left: 0; top: 457px; width: 840px; height: 23px;
    background: linear-gradient(90deg, #a00000, var(--brand-red) 50%, #a00000);
  }
  .footer__corner { position: absolute; right: 0; top: 0; }
</style>
</head>
<body>
  <section class="card card--front">
    <p class="front__tagline">WE HELP YOU MOVE ON!</p>
    <p class="front__name">SUMMIT</p>
    <p class="front__sub">HOME BUYERS</p>
  </section>

  <section class="card card--back">
    <div class="back__hero"></div>
    <svg class="back__slash" width="840" height="256" viewBox="0 0 840 256">
      <polygon points="840,78 840,117 621,256 601,256" fill="var(--white)"/>
      <polygon points="840,117 840,256 621,256" fill="var(--black)"/>
    </svg>
    <div class="back__person">
      <p class="person__name">Dale Morrow</p>
      <p class="person__title">President</p>
    </div>

    <div class="back__info">
      <svg class="icon" style="left:46px;top:18px" width="22" height="22" viewBox="0 0 24 24">
        <path d="M6.6 10.8a15 15 0 0 0 6.6 6.6l2.2-2.2a1 1 0 0 1 1-.25 11.4 11.4 0 0 0 3.6.57 1 1 0 0 1 1 1V20a1 1 0 0 1-1 1A17 17 0 0 1 3 4a1 1 0 0 1 1-1h3.5a1 1 0 0 1 1 1c0 1.250.2 2.450.57 3.57a1 1 0 0 1-.25 1z" fill="var(--ink)"/>
      </svg>
      <svg class="icon" style="left:44px;top:50px" width="28" height="26" viewBox="0 0 28 26">
        <rect x="2" y="9" width="24" height="15" fill="none" stroke="var(--ink)" stroke-width="2"/>
        <polyline points="2,9 14,18 26,9" fill="none" stroke="var(--ink)" stroke-width="2"/>
        <rect x="7" y="2" width="14" height="10" fill="none" stroke="var(--ink)" stroke-width="1.6"/>
        <line x1="10" y1="6" x2="18" y2="6" stroke="var(--ink)" stroke-width="1.4"/>
      </svg>
      <svg class="icon" style="left:32px;top:92px" width="50" height="48" viewBox="0 0 50 48">
        <path d="M25 2a11 11 0 0 0-11 11c0 8 11 20 11 20s11-12 11-20A11 11 0 0 0 25 2z" fill="var(--ink)"/>
        <circle cx="25" cy="13" r="4.5" fill="#dcdcdc"/>
        <polyline points="2,46 10,36 20,40 30,34 40,38 48,34 42,44 32,41 22,46 12,42 2,46" fill="none" stroke="var(--ink)" stroke-width="1.8"/>
      </svg>
      <p class="contact contact__phone">316-555-0148</p>
      <p class="contact contact__email">dale@prairiehomesforcash.com</p>
      <p class="contact contact__address">Optional address:<br>P.O. Box 112<br>Maple Ridge, KS 67010</p>

      <div class="mini-logo">
        <p class="mini-logo__tagline">WE HELP YOU MOVE ON!</p>
        <p class="mini-logo__name">SUMMIT</p>
        <p class="mini-logo__sub">HOME BUYERS</p>
      </div>
    </div>

    <p class="back__web">www.prairiehomesforcash.com</p>
    <div class="back__footer">
      <svg class="footer__corner" width="30" height="23" viewBox="0 0 30 23">
        <polygon points="0,0 30,0 30,23" fill="var(--black)"/>
      </svg>
    </div>
  </section>
</body>
</html>
```